Creative Website Design for Post Production Sound Editorial Company

We are seeking a highly creative and talented web designer to lead the transformation of our existing website into a visually captivating and user-friendly online platform for our Post Production Sound Editorial Company. As a specialized provider of sound editing services for diverse media productions, we recognize the critical importance of a compelling online presence that reflects our expertise and brand identity.
Project Overview:
Our website is already active and hosted via WordPress at https://pagecrate.example/view/velmortaudiocraft.example. Note: The brand book is in the guide. While it serves as a foundation, we are committed to elevating its impact by entrusting you with the task of enhancing its design, functionality, and user experience.

Target Market(s)

* Film Producers: Producers involved in film production, including directors, executive producers, and independent filmmakers, who require high-quality sound editing services to enhance their cinematic projects. * Television Producers: Producers responsible for television shows, series, and documentaries seeking post-production sound editing expertise to improve the audio quality of their content. * Podcast Producers: Podcast creators and producers in need of sound editorial services to enhance the audio experience and professionalism of their podcasts. * Advertising Agencies: Agencies working on multimedia advertising campaigns that require sound editing for commercials, promotional videos, and branded content. * Corporate Video Producers: Professionals responsible for producing corporate videos, training materials, and presentations that require polished and clear audio. * Documentary Filmmakers: Filmmakers creating documentary films who require sound editing to improve the audio clarity and storytelling impact of their projects. * Online Content Creators: Influencers, vloggers, and content creators producing online videos and multimedia content looking to enhance the audio quality of their productions. * Post-Production Studios: Post-production studios that may require specialized sound editing services for their clients, such as major film studios and media companies. * Event Planners: Event planners and organizers who need sound editing for event recordings, promotional videos, and multimedia presentations. * Educational Institutions: Educational institutions, including universities and schools, seeking sound editing services for educational videos, e-learning materials, and multimedia resources. * Government and Nonprofit Organizations: Government agencies and nonprofit organizations in need of sound editing services for public service announcements, informational videos, and awareness campaigns. * Streaming Platforms: Streaming platforms and online content distribution channels that require high-quality sound editing for their content libraries.

Industry/Entity Type

"Media and Entertainment." "Post-Production Services" or "Audio Post-Production Services."

Coding

Coded - Design and coding required

Number of Pages Required

5+ page

Font styles to use
Other font styles liked:
• Nexa

Colors

Designer to choose only greyscale colors for use in the design.

Requirements
Must have
• * Clean and Modern Design: Use a clean and contemporary design with a minimalist aesthetic. This will convey professionalism and make it easy for visitors to navigate our site. * High-Quality Imagery and Multimedia: Incorporate high-resolution images, video clips, and audio samples that showcase our work and expertise. Visual and auditory elements are essential in the sound editing industry. * Color Palette: Use Branding Kit for the color palette * Typography: Use Branding Kit (Nexa) to select clear, legible fonts for easy reading. * Responsive Design: Ensure that the website is fully responsive, adapting seamlessly to various screen sizes and devices. This is crucial for user-friendliness and accessibility. * Intuitive Navigation: Design a user-friendly navigation menu with clear headings and categories. Users should easily find information about our services, portfolio, about the company, and contact details. * Video Backgrounds: Consider using video backgrounds on the homepage or specific sections to capture attention and highlight our expertise. Ensure that the videos are relevant to our services. * Testimonials and Case Studies: Include client testimonials and case studies to build trust and credibility. Showcase successful projects we've worked on and the positive impact our sound editing services have had. * Interactive Elements: Incorporate interactive elements such as buttons, hover effects, and animations to engage visitors and make the website more dynamic. * Call-to-Action (CTA) Buttons: Strategically place CTA buttons throughout the site to encourage visitors to get in touch, request a quote, or explore our portfolio. * Contact Information: Make it easy for visitors to contact us by placing clear contact information, including a contact form, phone number, and email address. * Social Media Integration: Connect your social media profiles to the website to foster engagement and allow visitors to follow your updates. * Accessibility Features: Ensure that the website is accessible to all users, including those with disabilities. This includes using alt text for images and ensuring keyboard navigation is smooth. * Loading Speed: Optimize the website's loading speed to provide a seamless browsing experience. * Security: Implement security measures to protect user data and maintain trust.
Nice to have
• * Testimonials and Case Studies: Include client testimonials and case studies to build trust and credibility. Showcase successful projects you've worked on and the positive impact your sound editing services have had. * Blog Section: Include a blog section where you can share industry insights, tips, and updates. This can position your company as an authority in sound editing.
Should not have
• designers who are inexperienced

```html
<!DOCTYPE html>
<html lang="en">
<head>
<meta charset="utf-8">
<title>Velmort Audiocraft — Post-Production Sound Editorial</title>
<link rel="stylesheet" href="https://fonts.googleapis.com/css2?family=Ubuntu:wght@400;500;700&family=Open+Sans:wght@400;600;700&display=swap">
<style>
:root{
  --ink:#111111;
  --charcoal:#222222;
  --dark-band:#1f1f1f;
  --graphite:#333333;
  --text:#444444;
  --muted:#777777;
  --line:#dddddd;
  --frame:#e2e2e2;
  --paper:#ffffff;
  --mist-left:#f4f3f3;
  --mist-right:#ebeaea;
}
*{margin:0;padding:0;box-sizing:border-box}
html,body{width:1200px;height:4257px;overflow:hidden;background:var(--paper)}
body{font-family:"Open Sans",Arial,sans-serif;color:var(--text);position:relative}
.abs{position:absolute}
.display{font-family:"Ubuntu",Arial,sans-serif}

/* header */
.site-header{left:0;top:0;width:1200px;height:86px;background:var(--paper)}
.brand{left:111px;top:22px;font-family:"Ubuntu",sans-serif;font-size:31px;font-weight:500;color:var(--ink)}
.main-nav{left:547px;top:33px;display:flex;gap:24px;font-size:15px;color:var(--graphite)}
.btn-dark{background:var(--graphite);color:#fff;font-weight:700;font-size:15px;display:flex;align-items:center;justify-content:center}
.quote-btn{left:922px;top:21px;width:166px;height:42px}

/* hero */
.hero{left:0;top:86px;width:1200px;height:471px;background:radial-gradient(circle at 30% 35%,#8a7a5e 0%,#4a3c2a 35%,#2a2118 70%,#140f0b 100%)}
.play{left:306px;top:209px}
.hero-card{left:565px;top:152px;width:523px;height:339px;background:rgba(20,20,20,.86);border-radius:6px;padding:44px 36px 0}
.hero-card h1{font-family:"Ubuntu",sans-serif;font-weight:500;font-size:32px;line-height:38px;color:#fff}
.hero-card p{margin-top:17px;font-size:15px;line-height:28px;color:#eee}
.hero-card .link{margin-top:14px;margin-left:7px;display:inline-block;font-size:15px;font-weight:700;color:#fff;text-decoration:underline}

/* about */
.about-title{left:113px;top:630px;font-family:"Ubuntu",sans-serif;font-weight:700;font-size:36px;color:var(--ink)}
.about-sub{left:113px;top:686px;font-family:"Ubuntu",sans-serif;font-weight:500;font-size:23px;color:var(--graphite)}
.about-text{left:111px;top:749px;width:580px;font-size:15px;line-height:28px;color:var(--text)}
.about-btn{left:111px;top:1017px;width:124px;height:38px}
.about-frame{left:732px;top:612px;width:331px;height:441px;background:var(--frame)}
.about-photo{left:759px;top:636px;width:329px;height:444px;background:linear-gradient(160deg,#7a2d5c 0%,#3b1a3a 45%,#1a1420 100%)}

/* alchemy */
.alchemy{left:0;top:1134px;width:1200px;height:504px;background:var(--dark-band)}
.centered{left:0;width:1200px;text-align:center}
.alchemy-title{top:1215px;font-family:"Ubuntu",sans-serif;font-weight:700;font-size:34px;color:#fff}
.alchemy-sub{top:1271px;font-family:"Ubuntu",sans-serif;font-weight:500;font-size:22px;color:#e6e6e6}
.alchemy-frame{left:127px;top:1373px;width:364px;height:330px;background:var(--frame)}
.alchemy-photo{left:111px;top:1359px;width:363px;height:350px;background:radial-gradient(circle at 55% 45%,#4d6b8f 0%,#26344a 45%,#12161f 100%)}
.alchemy-text{left:565px;top:1392px;width:525px;font-size:15px;line-height:28px;color:#f0f0f0}
.btn-outline{border:1px solid #fff;color:#fff;font-weight:700;font-size:15px;display:flex;align-items:center;justify-content:center}
.alchemy-btn{left:565px;top:1534px;width:124px;height:41px}

/* cards */
.section-title{font-family:"Ubuntu",sans-serif;font-weight:700;font-size:36px;color:var(--ink)}
.card-photo{width:317px;height:216px}
.card{width:301px;height:233px;background:#fff;box-shadow:0 3px 10px rgba(0,0,0,.14);padding:30px 28px 0}
.card .meta{font-size:14px;color:var(--muted)}
.card h3{margin-top:16px;font-size:17px;font-weight:600;color:var(--ink)}
.card p{margin-top:14px;font-size:15px;line-height:28px;color:var(--text)}

/* testimonials */
.testimonials{left:0;top:2443px;width:1200px;height:453px;background:radial-gradient(ellipse at 50% 40%,#3a3a3a 0%,#222 55%,#161616 100%)}
.testi-title{top:2520px;font-family:"Ubuntu",sans-serif;font-weight:700;font-size:36px;color:#fff}
.testi-text{left:150px;width:900px;top:2706px;text-align:center;font-size:15.5px;line-height:27px;color:#f2f2f2}
.testi-name{top:2812px;font-size:15px;font-weight:600;color:#fff}

/* contact */
.contact-left{left:0;top:3599px;width:628px;height:482px;background:var(--mist-left)}
.contact-right{left:628px;top:3599px;width:572px;height:482px;background:var(--mist-right)}
.form-title{left:109px;top:3662px}
.field{background:#fff;height:47px;padding:14px 14px;font-size:15px;color:var(--muted)}
.contact-title{left:693px;top:3657px}
.contact-item{left:693px;display:flex;gap:18px;align-items:flex-start;font-size:16px;line-height:30px;color:var(--ink)}
.social{left:697px;top:3962px;display:flex;gap:12px}
.social span{width:23px;height:23px;background:var(--ink);border-radius:3px;display:block}

/* footer */
.site-footer{left:0;top:4081px;width:1200px;height:176px;background:var(--charcoal)}
.footer-brand{top:4124px;font-family:"Ubuntu",sans-serif;font-weight:500;font-size:32px;color:#fff}
.footer-copy{top:4181px;font-size:16px;color:#eee}
</style>
</head>
<body>

<header class="site-header abs">
  <div class="brand abs">Velmort Audiocraft</div>
  <nav class="main-nav abs"><span>Home</span><span>About</span><span>Work</span><span>Services</span><span>Contact</span></nav>
  <div class="quote-btn btn-dark abs">Request a Quote</div>
</header>

<section class="hero abs" role="img" aria-label="Studio microphones over a lit mixing console"></section>
<svg class="play abs" width="54" height="54" viewBox="0 0 54 54" aria-label="Play video">
  <circle cx="27" cy="27" r="25" fill="#fff" stroke="#222" stroke-width="3"/>
  <path d="M21 16 L38 27 L21 38 Z" fill="#222"/>
</svg>
<div class="hero-card abs">
  <h1>Bringing Your Story to Life Through the Power of Sound</h1>
  <p>Welcome to Velmort Audiocraft, the premier destination for post-production sound editing services. With over 20 years of experience in the industry, our owner brings a wealth of expertise and knowledge to every project.</p>
  <span class="link">READ MORE</span>
</div>

<h2 class="about-title abs">VELMORT AUDIOCRAFT</h2>
<div class="about-sub abs">ENTER A WORLD OF SONIC EXCELLENCE</div>
<p class="about-text abs">Welcome to Velmort Audiocraft, where sound becomes an extraordinary symphony of artistry. Immerse yourself in a captivating world where every audio element is meticulously crafted to evoke emotions and enhance storytelling. Our team of experienced sound editors and engineers are passionate about delivering sonic excellence, creating immersive experiences that transport audiences to new dimensions. Get ready to embark on a sonic journey like no other, where every note, rhythm, and sound effect harmonizes to create a symphony of audio perfection.</p>
<div class="about-btn btn-dark abs">Read More</div>
<div class="about-frame abs"></div>
<div class="about-photo abs" role="img" aria-label="Recording studio desk with monitors in magenta light"></div>

<section class="alchemy abs"></section>
<h2 class="alchemy-title centered abs">SONIC ALCHEMY</h2>
<div class="alchemy-sub centered abs">TRANSFORMING SOUND INTO CAPTIVATING EXPERIENCES</div>
<div class="alchemy-frame abs"></div>
<div class="alchemy-photo abs" role="img" aria-label="Condenser microphone on a stand in a dim studio"></div>
<p class="alchemy-text abs">At Velmort Audiocraft, we possess the secret of sonic alchemy, the art of transforming sound into captivating experiences. Our range of expert services includes dialogue editing, sound effects editing, foley editing, ADR editing, and mixing.</p>
<div class="alchemy-btn btn-outline abs">Read More</div>

<h2 class="section-title centered abs" style="top:1806px">LATEST BLOG</h2>
<div class="card-photo abs" style="left:111px;top:1906px;background:linear-gradient(160deg,#8a5a3a,#3a2a22)" role="img" aria-label="Crowd browsing records at a vinyl fair"></div>
<div class="card-photo abs" style="left:441px;top:1906px;background:linear-gradient(160deg,#a06a50,#d8d4cf)" role="img" aria-label="Two editors reviewing a project on a monitor"></div>
<div class="card-photo abs" style="left:772px;top:1906px;background:linear-gradient(160deg,#5a4030,#1e1a18)" role="img" aria-label="Sound engineer with headphones at a mixing desk"></div>
<article class="card abs" style="left:119px;top:2103px"><div class="meta">04-09-2022 | By Mara Quillon</div><h3>Sed ut perspiciatis unde omnis</h3><p>Sed ut perspiciatis unde omnis iste natus error sit voluptatem accusan-tium doloremque</p></article>
<article class="card abs" style="left:450px;top:2103px"><div class="meta">04-09-2022 | By Mara Quillon</div><h3>Sed ut perspiciatis unde omnis</h3><p>Sed ut perspiciatis unde omnis iste natus error sit voluptatem accusan-tium doloremque</p></article>
<article class="card abs" style="left:780px;top:2103px"><div class="meta">04-09-2022 | By Mara Quillon</div><h3>Sed ut perspiciatis unde omnis</h3><p>Sed ut perspiciatis unde omnis iste natus error sit voluptatem accusan-tium doloremque</p></article>

<section class="testimonials abs" role="img" aria-label="Darkened studio headphones and console backdrop"></section>
<h2 class="testi-title centered abs">TESTIMONIALS</h2>
<svg class="abs" style="left:573px;top:2623px" width="54" height="54" viewBox="0 0 54 54" aria-label="Quote">
  <circle cx="27" cy="27" r="25" fill="none" stroke="#fff" stroke-width="2.5"/>
  <text x="27" y="38" text-anchor="middle" font-family="Georgia,serif" font-size="30" fill="#fff">99</text>
</svg>
<p class="testi-text abs">Lorem ipsum dolor sit amet, consectetur adipiscing elit, sed do eiusmod tempor incididunt ut labore et dolore magna aliqua. Ut enim ad minim veniam, quis nostrud exercitation ullamco laboris nisi ut aliquip ex ea commodo consequat. Duis aute irure dolor in reprehenderit in voluptate velit esse cillum dolore eu fugiat nulla pariatur.</p>
<div class="testi-name centered abs">LENA R.</div>

<h2 class="section-title centered abs" style="top:2998px">CASE STUDIES</h2>
<div class="card-photo abs" style="left:111px;top:3098px;background:linear-gradient(160deg,#2c5a78,#12202c)" role="img" aria-label="Audio editing timeline on a screen"></div>
<div class="card-photo abs" style="left:441px;top:3098px;background:linear-gradient(160deg,#8a2a2a,#1a1416)" role="img" aria-label="Producer playing a keyboard in a studio"></div>
<div class="card-photo abs" style="left:772px;top:3098px;background:linear-gradient(160deg,#b07a4a,#3a3636)" role="img" aria-label="Editing workstation with waveforms on monitors"></div>
<article class="card abs" style="left:119px;top:3294px"><div class="meta">04-09-2022 | By Mara Quillon</div><h3>Sed ut perspiciatis unde omnis</h3><p>Sed ut perspiciatis unde omnis iste natus error sit voluptatem accusan-tium doloremque</p></article>
<article class="card abs" style="left:450px;top:3294px"><div class="meta">04-09-2022 | By Mara Quillon</div><h3>Sed ut perspiciatis unde omnis</h3><p>Sed ut perspiciatis unde omnis iste natus error sit voluptatem accusan-tium doloremque</p></article>
<article class="card abs" style="left:780px;top:3294px"><div class="meta">04-09-2022 | By Mara Quillon</div><h3>Sed ut perspiciatis unde omnis</h3><p>Sed ut perspiciatis unde omnis iste natus error sit voluptatem accusan-tium doloremque</p></article>

<section class="contact-left abs"></section>
<section class="contact-right abs"></section>
<h2 class="section-title form-title abs">REQUEST A QUOTE</h2>
<div class="field abs" style="left:109px;top:3738px;width:230px">Name:</div>
<div class="field abs" style="left:349px;top:3738px;width:230px">Age</div>
<div class="field abs" style="left:109px;top:3797px;width:230px">Email:</div>
<div class="field abs" style="left:349px;top:3797px;width:230px">Phone:</div>
<div class="field abs" style="left:109px;top:3856px;width:470px;height:96px">Message:</div>
<div class="btn-dark abs" style="left:109px;top:3979px;width:126px;height:41px">Get in touch</div>

<h2 class="section-title contact-title abs">CONTACT US</h2>
<div class="contact-item abs" style="top:3744px">
  <svg width="28" height="36" viewBox="0 0 24 32"><path d="M12 0C5.4 0 0 5.2 0 11.7 0 20 12 32 12 32s12-12 12-20.3C24 5.2 18.6 0 12 0zm0 16a4.5 4.5 0 1 1 0-9 4.5 4.5 0 0 1 0 9z" fill="#111"/></svg>
  <span>Velmort Audiocraft,<br>Address Comes Here</span>
</div>
<div class="contact-item abs" style="top:3828px">
  <svg width="30" height="30" viewBox="0 0 24 24"><path d="M6.6 10.8a15.1 15.1 0 0 0 6.6 6.6l2.2-2.2c.3-.3.7-.4 1-.2 1.1.4 2.3.6 3.6.6.6 0 1 .4 1 1V20c0 .6-.4 1-1 1A17 17 0 0 1 3 4c0-.6.4-1 1-1h3.5c.6 0 1 .4 1 1 0 1.3.2 2.5.6 3.6.1.3 0 .7-.2 1z" fill="#111"/></svg>
  <span>917-555-0186</span>
</div>
<div class="contact-item abs" style="top:3893px">
  <svg width="30" height="30" viewBox="0 0 24 24"><path d="M2 5h20v14H2z" fill="#111"/><path d="M3 6l9 7 9-7" fill="none" stroke="#fff" stroke-width="1.6"/></svg>
  <span>info@velmortaudiocraft.example</span>
</div>
<div class="social abs" aria-label="Social profiles"><span></span><span></span><span></span><span></span></div>

<footer class="site-footer abs"></footer>
<div class="footer-brand centered abs">Velmort Audiocraft</div>
<div class="footer-copy centered abs">2023 Velmort Audiocraft. All Rights Reserved.</div>

</body>
</html>
```